Book Cover "Gilded"

Book summary:

Mara Dunholt emerged from the oily wash of the Seine five years ago with no memory of her life, but an uncanny knowledge of fine art, museum security, and a knack for walking away with priceless treasures. Now she's tracking an elusive De Marsk with ties to an underworld struggle that will reveal her forgotten past. 

She leaves Paris to track a priceless painting from St. Pete to Chicago. Her contacts are shady and she is beginning to think there is more to this job than a buyer wanting a gift for his wife. Otherwise, why would Felix Armistead, a rival thief, cross her path just as the BCX begins asking questions?

Caught up in the six billion dollar international art theft industry, she enlists help from unlikely sources: film actor Neil Barto, and veteran BCX specialists Graham Pellow and Peter Lasky.

>> This novel is currently on Readlooma.com with free sample downloads available.

>> This is the first book in a series - future titles will also feature art crime suspense theme, with international locations.

>> eBook file available upon request via email.

```html
<!DOCTYPE html>
<html lang="en">
<head>
<meta charset="utf-8">
<title>Gilded — Lena Harrow</title>
<link rel="stylesheet" href="https://fonts.googleapis.com/css2?family=Ultra&family=EB+Garamond:ital@1&display=swap">
<style>
  :root {
    --paper-light: #d4a27c;
    --paper-mid: #c08660;
    --paper-dark: #9c6440;
    --string: #c9a26a;
    --frame-outer: #b8692a;
    --frame-outer-dark: #8a4a1c;
    --frame-gold: #e39a2c;
    --frame-gold-light: #f6c25a;
    --skyline-paper: #ecd8b4;
    --skyline-ink: #1b1510;
    --band-edge: #e2b777;
    --band-yellow: #fef22a;
    --ink: #111111;
  }
  html, body {
    margin: 0;
    padding: 0;
    overflow: hidden;
    background: #ffffff;
  }
  .cover {
    position: relative;
    width: 900px;
    height: 1200px;
    overflow: hidden;
    background: radial-gradient(ellipse at 50% 40%, var(--paper-light) 0%, var(--paper-mid) 55%, var(--paper-dark) 100%);
  }
  .hanging-frame {
    position: absolute;
    inset: 0;
  }
  .title-band {
    position: absolute;
    left: 0;
    top: 792px;
    width: 900px;
    height: 252px;
    background: var(--band-edge);
  }
  .title-band__inner {
    position: absolute;
    left: 0;
    right: 0;
    top: 18px;
    bottom: 18px;
    background: var(--band-yellow);
    display: flex;
    align-items: center;
    justify-content: center;
  }
  .title {
    margin: 0;
    font-family: "Ultra", "Cooper Black", serif;
    font-weight: 400;
    font-size: 180px;
    line-height: 1;
    letter-spacing: 0;
    color: var(--ink);
    transform: translateY(4px);
  }
  .author {
    position: absolute;
    right: 28px;
    top: 1062px;
    margin: 0;
    font-family: "EB Garamond", Georgia, serif;
    font-style: italic;
    font-size: 96px;
    line-height: 1;
    color: var(--ink);
  }
</style>
</head>
<body>
<main class="cover">
  <svg class="hanging-frame" width="900" height="1200" viewBox="0 0 900 1200">
    <defs>
      <linearGradient id="skyline-fill" x1="0" y1="0" x2="0" y2="1">
        <stop offset="0" stop-color="var(--skyline-paper)" stop-opacity="0"/>
        <stop offset="0.3" stop-color="var(--skyline-paper)" stop-opacity="0.85"/>
        <stop offset="0.6" stop-color="#5a4230"/>
        <stop offset="1" stop-color="var(--skyline-ink)"/>
      </linearGradient>
    </defs>
    <g class="hanging-string" stroke="var(--string)" stroke-width="5" fill="none" stroke-linecap="round">
      <line x1="258" y1="0" x2="152" y2="262"/>
      <line x1="552" y1="0" x2="785" y2="282"/>
    </g>
    <g class="picture-frame" transform="rotate(-12.5 460 495)">
      <rect class="frame-outer" x="80" y="240" width="760" height="510" fill="var(--frame-outer)" stroke="var(--frame-outer-dark)" stroke-width="4"/>
      <rect class="frame-moulding" x="138" y="296" width="644" height="398" fill="var(--frame-gold)"/>
      <rect class="frame-moulding-highlight" x="146" y="304" width="628" height="382" fill="none" stroke="var(--frame-gold-light)" stroke-width="4"/>
      <rect class="frame-opening" x="162" y="320" width="596" height="350" fill="var(--paper-mid)"/>
      <rect class="skyline" role="img" aria-label="Torn-paper silhouette of the Paris skyline with the Eiffel Tower and domed landmarks" x="162" y="450" width="596" height="220" fill="url(#skyline-fill)"/>
    </g>
  </svg>

  <div class="title-band">
    <div class="title-band__inner">
      <h1 class="title">GILDED</h1>
    </div>
  </div>

  <p class="author">Lena Harrow</p>
</main>
</body>
</html>
```